Web Design for TV Mounting & Appliance Repair Company

We need a website design for the homepage and one inner page for a TV Mounting & Appliance Repair company.
The goal is to promote the company's services and provide information about the company.
TV Mounting & Appliance Repair Company Homepage:
-Banner with company name (Braylo) and slogan (e.g. "Your One Stop Shop for TV Mounting and Appliance Repair")
-Overview/content of services offered (TV mounting, appliance repair)
-Call to action buttons (e.g. "Schedule a Service", "Request a Quote")
-Location and contact information (please create a map of East coast of from Maine to Virginia)
Number of Pages Required
2 page
Font styles to use
Colors
Designer to choose colors to be used in the design.
Look and feel
Each slider illustrates characteristics of the customer's brand and the style your logo design should communicate.

```html
<!DOCTYPE html>
<html lang="en">
<head>
<meta charset="utf-8">
<title>Braylo — TV Mounting &amp; Appliance Repair</title>
<link href="https://fonts.googleapis.com/css2?family=Poppins:wght@400;500;600;700&family=Lora:wght@400;500&display=swap" rel="stylesheet">
<style>
:root{
  --orange:#ef5a24;
  --orange-deep:#e04d1a;
  --black:#111111;
  --ink:#222222;
  --text:#555555;
  --grey-bg:#efefef;
  --card:#ffffff;
}
*{margin:0;padding:0;box-sizing:border-box}
html,body{width:1200px;height:4130px;overflow:hidden;background:#fff}
body{font-family:'Poppins',sans-serif;color:var(--ink)}
.page{position:relative;width:1200px;height:4130px;overflow:hidden}
.abs{position:absolute}
.photo{position:absolute;overflow:hidden}

/* header */
.logo{left:100px;top:38px;display:flex;align-items:center;gap:12px;font-size:44px;font-weight:700;color:var(--orange);letter-spacing:.5px}
.logo-dot{width:18px;height:18px;border-radius:50%;background:var(--black)}
.nav{left:315px;top:30px;width:620px;height:64px;border-radius:32px;background:rgba(255,255,255,.85);display:flex;align-items:center;gap:28px;padding-left:25px;font-size:19px;font-weight:500;color:var(--ink)}
.btn-login{left:933px;top:38px;width:168px;height:50px;border-radius:25px;background:var(--orange);color:#fff;font-weight:600;font-size:21px;display:flex;align-items:center;justify-content:center}

/* hero */
.hero-welcome{left:100px;top:258px;font-size:31px;font-weight:400;color:var(--ink);display:flex;align-items:center;gap:16px}
.hero-welcome b{color:var(--orange);font-weight:700}
.hero-slogan{left:100px;top:316px;font-size:22px;line-height:34px;font-weight:500;color:var(--ink)}
.btn-square{background:var(--orange);color:#fff;font-weight:600;display:flex;align-items:center;justify-content:center;box-shadow:5px 5px 0 var(--black)}
.btn-schedule{left:100px;top:404px;width:212px;height:48px;font-size:18px}

/* about */
.about-photo{left:100px;top:748px;width:478px;height:428px;border-top-right-radius:140px;border-bottom-left-radius:70px;background:linear-gradient(135deg,#bfb6ad,#d9cdc2 55%,#a58b74);box-shadow:12px 12px 0 var(--black)}
.section-title{font-size:34px;font-weight:400;color:var(--orange)}
.about-title{left:638px;top:785px}
.body-serif{font-family:'Lora',serif;font-size:14.5px;line-height:25.6px;color:var(--text);text-align:justify}
.about-text{left:638px;top:845px;width:463px}
.btn-read{font-family:'Lora',serif;font-size:21px;font-weight:500}
.about-read{left:638px;top:1101px;width:155px;height:48px}

/* mounting band */
.band{left:0;top:1276px;width:1200px;height:233px;background:var(--orange)}
.band-title{left:0;top:1316px;width:1200px;text-align:center;color:#fff;font-size:30px;font-weight:600}
.svc-card{top:1397px;width:243px;height:201px;background:var(--card);border-radius:8px;box-shadow:0 3px 10px rgba(0,0,0,.15);display:flex;flex-direction:column;align-items:center;padding-top:24px}
.svc-card svg{width:115px;height:115px}
.svc-card span{margin-top:20px;font-size:21px;font-weight:500;color:var(--ink)}

/* appliance */
.appliance{left:0;top:1688px;width:1200px;height:767px;background:var(--grey-bg)}
.tile{width:262px;border-radius:10px;color:#fff;font-weight:600;font-size:16px}
.tile-label{position:absolute;left:0;right:0;bottom:28px;text-align:center}
.tile-fridge{left:100px;top:1786px;height:292px;background:var(--orange);padding:40px 20px 0;text-align:center}
.tile-fridge h4{font-size:16px;font-weight:600}
.tile-fridge p{font-family:'Lora',serif;font-weight:400;font-size:17px;line-height:26px;margin-top:10px}
.tile-fridge a{display:inline-block;font-family:'Lora',serif;font-size:17px;text-decoration:underline;margin-top:14px;color:#fff}
.tile-wash{left:408px;top:1752px;height:291px;background:linear-gradient(160deg,#e8e8e8,#8d9aa4 60%,#5b6670)}
.tile-dryer{left:100px;top:2107px;height:290px;background:linear-gradient(160deg,#9aa0a4,#cfc9c2 55%,#6d7378)}
.tile-dish{left:408px;top:2073px;height:290px;background:linear-gradient(160deg,#c0392b,#6b6f74 50%,#2d3034)}
.our-service{left:718px;top:1838px;font-size:30px}
.appliance-title{left:718px;top:1885px;font-size:30px;font-weight:600;line-height:40px;color:var(--ink)}
.appliance-text{left:718px;top:1980px;width:383px}
.appliance-read{left:720px;top:2162px;width:155px;height:48px}

/* testimonials */
.center-title{left:0;width:1200px;text-align:center;font-size:29px;font-weight:600;color:var(--ink);line-height:43px}
.review{top:2650px;width:310px;height:212px;background:#fff;border-radius:12px;box-shadow:0 2px 10px rgba(0,0,0,.18);text-align:center;padding-top:60px}
.review h3{font-size:25px;font-weight:600}
.review h5{font-size:16px;font-weight:600;margin-top:8px}
.review p{font-family:'Lora',serif;font-size:12.5px;line-height:20px;color:#444;margin:6px 28px 0}
.avatar{top:2603px;width:88px;height:88px;border-radius:50%;background:linear-gradient(180deg,#d8d8d8,#8a8a8a);border:4px solid #fff;box-shadow:0 2px 6px rgba(0,0,0,.2)}

/* map */
.map{left:250px;top:3070px;width:700px;height:440px;border-radius:40px 60px 30px 80px;background:radial-gradient(circle at 82% 55%,rgba(239,90,36,.55) 0,rgba(239,90,36,0) 9%),linear-gradient(135deg,#2b2b2b,#3a3a3a)}

/* cta & footer */
.footer-bg{left:0;top:3600px;width:1200px;height:530px}
.cta{left:100px;top:3560px;width:1000px;height:106px;background:var(--orange);border-radius:10px}
.cta-text{left:123px;top:3596px;font-size:26px;font-weight:600;color:#fff}
.cta-btn{left:824px;top:3578px;width:248px;height:70px;border-radius:35px;background:#fff;color:var(--orange);font-size:21px;font-weight:500;display:flex;align-items:center;justify-content:center}
.f-col{top:3742px;color:#fff}
.f-col h4{font-size:20px;font-weight:500;position:relative;padding-bottom:14px}
.f-col h4::after{content:"";position:absolute;left:0;bottom:0;width:28px;height:3px;background:var(--orange)}
.f-col ul{list-style:none;margin-top:14px;font-size:13px;line-height:30px}
.f-col p{font-size:13.5px;line-height:23px}
.socials{left:306px;top:3937px;display:flex;gap:8px}
.socials i{display:block;width:30px;height:30px;border-radius:50%;border:1.5px solid #fff}
.email-field{left:810px;top:3870px;width:276px;height:38px;border-radius:19px;background:#fff;font-size:12px;color:#555;display:flex;align-items:center;justify-content:space-between;padding:0 12px 0 18px}
.email-field b{width:20px;height:20px;border-radius:50%;background:var(--black);display:flex;align-items:center;justify-content:center}
.bottom-bar{left:0;top:4062px;width:1200px;height:68px;background:#2b2b2b;color:#fff;font-size:15px;display:flex;align-items:center;justify-content:space-between;padding:0 120px 0 112px}
</style>
</head>
<body>
<div class="page">

  <svg class="abs" style="left:0;top:0" width="1200" height="670" viewBox="0 0 1200 670">
    <rect width="1200" height="670" fill="#f6f6f6"/>
    <path d="M0 420 C120 470 200 560 420 620 C700 690 1000 650 1200 650 L1200 670 L0 670Z" fill="#fff"/>
    <path d="M0 430 C150 470 230 560 460 612 C640 650 900 648 1200 648 L1200 660 C900 662 620 664 420 640 C240 615 120 560 0 520Z" fill="var(--orange)"/>
    <path d="M0 500 C120 560 240 610 440 640 C700 665 950 655 1200 660 L1200 666 C950 668 650 672 420 655 C230 640 110 610 0 600Z" fill="var(--black)"/>
  </svg>
  <div class="photo" role="img" aria-label="Two technicians mounting a flat-screen TV on a living room wall" style="left:630px;top:-40px;width:640px;height:610px;border-radius:50%;background:linear-gradient(200deg,#d9d4cf,#b8aea4 55%,#7d7470)"></div>

  <div class="abs logo">Braylo<span class="logo-dot"></span></div>
  <nav class="abs nav"><span>Home</span><span>About</span><span>TV Installtion</span><span>Tv Mounting</span><span>Contact Us</span></nav>
  <div class="abs btn-login">LOGIN</div>

  <div class="abs hero-welcome">WELCOME TO <b>BRAYLO</b></div>
  <div class="abs hero-slogan">Your One Stop Shop for TV Mounting<br>and Appliance Repair</div>
  <div class="abs btn-square btn-schedule">Schedule a Service</div>

  <div class="photo about-photo" role="img" aria-label="Technician installing a TV bracket on a wall"></div>
  <h2 class="abs section-title about-title">ABOUT US</h2>
  <p class="abs body-serif about-text">Sed ut perspiciatis unde omnis iste natus error sit voluptatem accusantium doloremque laudantium, totam rem aperiam, eaque ipsa quae ab illo inventore veritatis et quasi architecto beatae vitae dicta sunt explicabo. Nemo enim ipsam voluptatem quia voluptas sit aspernatur aut odit aut fugit, sed quia consequuntur magni dolores eos qui ratione voluptatem sequi nesciunt. Neque porro quisquam est, qui dolorem ipsum quia dolor sit amet, consectetur, adipisci velit, sed quia non numquam eius modi tempora incidunt ut labore et dolore magnam aliquam quaerat voluptatem.</p>
  <div class="abs btn-square btn-read about-read">Read More</div>

  <div class="abs band"></div>
  <h2 class="abs band-title">LOOKING FOR A PROFESSIONAL TV MOUNTING</h2>

  <div class="abs svc-card" style="left:100px">
    <svg viewBox="0 0 100 100" fill="none" stroke="#111" stroke-width="3.5">
      <circle cx="48" cy="48" r="30"/><circle cx="48" cy="48" r="16"/>
      <path d="M48 10v8M48 78v8M10 48h8M78 48h8M21 21l6 6M69 69l6 6M21 75l6-6M69 27l6-6"/>
      <circle cx="74" cy="74" r="13" fill="#fff"/><path d="M67 74l5 5 9-9"/>
    </svg><span>INSTALLATION</span>
  </div>
  <div class="abs svc-card" style="left:355px">
    <svg viewBox="0 0 100 100" fill="none" stroke="#111" stroke-width="3.5">
      <rect x="12" y="12" width="76" height="16"/><rect x="12" y="32" width="76" height="16"/><rect x="12" y="52" width="76" height="16"/>
      <path d="M38 12v56M62 12v56M8 72h84M18 72v18M82 72v18M30 72v10M50 72v10M70 72v10"/>
    </svg><span>SECURING TV</span>
  </div>
  <div class="abs svc-card" style="left:606px">
    <svg viewBox="0 0 100 100" fill="none" stroke="#111" stroke-width="3.5">
      <rect x="10" y="26" width="80" height="54"/><rect x="16" y="32" width="68" height="42"/>
      <path d="M22 80v8M78 80v8M42 16a11 11 0 0 1 16 0M46 20a5 5 0 0 1 8 0"/>
    </svg><span>CONNECT TV</span>
  </div>
  <div class="abs svc-card" style="left:856px">
    <svg viewBox="0 0 100 100" fill="none" stroke="#111" stroke-width="3.5">
      <rect x="20" y="20" width="60" height="60"/><rect x="28" y="28" width="44" height="44"/><circle cx="50" cy="50" r="9"/>
      <path d="M30 8v12M42 8v12M58 8v12M70 8v12M30 80v12M42 80v12M58 80v12M70 80v12M8 30h12M8 42h12M8 58h12M8 70h12M80 30h12M80 42h12M80 58h12M80 70h12"/>
    </svg><span>HARDWARE</span>
  </div>

  <div class="abs appliance"></div>
  <div class="abs tile tile-fridge">
    <h4>REFRIGERATOR</h4>
    <p>Lorem ipsum dolor sit amet, consectetur adipiscing elit, sed do eiusmod tempor incididunt ut labore et dolore magna aliqua.</p>
    <a>LEARN MORE</a>
  </div>
  <div class="photo tile tile-wash" role="img" aria-label="Technician repairing a washing machine"><span class="tile-label">WASHING MACHINE</span></div>
  <div class="photo tile tile-dryer" role="img" aria-label="Smiling technician with clipboard beside a dryer"><span class="tile-label">DRYER</span></div>
  <div class="photo tile tile-dish" role="img" aria-label="Technician repairing a dishwasher"><span class="tile-label">DISHWASHER</span></div>

  <h2 class="abs section-title our-service">OUR SERVICE</h2>
  <h3 class="abs appliance-title">APPLIANCE REPAIR<br>SERVICE</h3>
  <p class="abs body-serif appliance-text" style="font-size:15.5px">If you are in need of appliance repair, our team at Braylo is here to help. We offer a wide range of appliance repair services, including refrigerator repair, oven repair, dishwasher repair, washer/dryer repair, and more. We understand the importance of having working appliances,</p>
  <div class="abs btn-square btn-read appliance-read">Read More</div>

  <h2 class="abs center-title" style="top:2535px">YOUR NEIGHBORS ARE OUR HAPPY CLIENTS</h2>
  <div class="abs review" style="left:103px"><h3>Dan R.</h3><h5>Somerville, MA</h5><p>The tech from Braylo was very thorough and took the time to answer all my questions.</p></div>
  <div class="abs review" style="left:445px"><h3>Megan T.</h3><h5>SomLong Island, NY</h5><p>The team was extremely professional and courteous, and they did a great job of mounting my TV.</p></div>
  <div class="abs review" style="left:785px"><h3>Kevin L.</h3><h5>Andover, NJ</h5><p>They were extremely professional and did a great job repairing our fridge.</p></div>
  <div class="photo avatar" role="img" aria-label="Client portrait" style="left:213px"></div>
  <div class="photo avatar" role="img" aria-label="Client portrait" style="left:556px"></div>
  <div class="photo avatar" role="img" aria-label="Client portrait" style="left:895px"></div>

  <h2 class="abs center-title" style="top:2950px">HAPPILY SERVING FAMILIES ON THE EAST COAST<br>FOR OVER 25 YEARS!</h2>
  <div class="photo map" role="img" aria-label="Map of the United States by state with Virginia highlighted, showing the East Coast service area from Maine to Virginia"></div>

  <svg class="abs footer-bg" viewBox="0 0 1200 530" width="1200" height="530">
    <rect x="0" y="20" width="1200" height="510" fill="var(--black)"/>
    <rect x="0" y="14" width="120" height="6" fill="var(--black)"/>
    <path d="M1100 0 C1150 20 1180 50 1200 70 L1200 220 C1180 180 1140 120 1100 80Z" fill="var(--orange)"/>
    <path d="M1090 0 L1200 0 L1200 60 C1170 30 1130 10 1090 0Z" fill="#fff"/>
  </svg>
  <div class="abs cta"></div>
  <div class="abs cta-text">START SCHEDULING YOUR SERVICE TODAY</div>
  <div class="abs cta-btn">REQUEST A QUOTE</div>

  <div class="abs f-col" style="left:110px"><h4>QUICK LINKS</h4><ul><li>Home</li><li>About</li><li>TV Installtion</li><li>Tv Mounting</li><li>Contact Us</li></ul></div>
  <div class="abs f-col" style="left:303px"><h4>OUR SERVICE</h4><ul><li>Refrigerator</li><li>washing machine</li><li>Dryer</li><li>Dishwasher</li></ul></div>
  <div class="abs socials"><i></i><i></i><i></i></div>
  <div class="abs f-col" style="left:522px;width:170px"><h4>CONTACT US</h4>
    <p style="margin-top:14px"><svg width="12" height="15" viewBox="0 0 12 15"><path d="M6 0a6 6 0 0 1 6 6c0 4-6 9-6 9S0 10 0 6a6 6 0 0 1 6-6z" fill="#fff"/><circle cx="6" cy="6" r="2.2" fill="#111"/></svg>&nbsp; ADDRESS</p>
    <p>201 Lorem ipsum dolor sit amet, consectetur adipiscing elit, sed do eiusmod tempor.</p>
    <p style="margin-top:8px">PHONE</p>
    <p><svg width="12" height="12" viewBox="0 0 24 24"><path d="M6.6 10.8a15 15 0 0 0 6.6 6.6l2.2-2.2a1 1 0 0 1 1-.25 11.4 11.4 0 0 0 3.6.57 1 1 0 0 1 1 1V20a1 1 0 0 1-1 1A17 17 0 0 1 3 4a1 1 0 0 1 1-1h3.5a1 1 0 0 1 1 1c0 1.25.2 2.45.57 3.57a1 1 0 0 1-.25 1z" fill="#fff"/></svg> +1 555-014-2298</p>
    <p style="margin-top:8px">EMAIL</p>
    <p>info@braylo.com</p>
  </div>
  <div class="abs f-col" style="left:812px;width:280px"><h4>EXCLUSIVE OFFERS</h4><p style="margin-top:14px">Subscribe to our newsletter for news and special offers</p></div>
  <div class="abs email-field">Enter Email<b><svg width="10" height="10" viewBox="0 0 10 10"><path d="M1 5h7M5 2l3 3-3 3" stroke="#fff" stroke-width="1.5" fill="none"/></svg></b></div>

  <div class="abs bottom-bar"><span>© copyrights 2022 © braylo| &nbsp;All Rights Reserved</span><span style="font-size:14px">Terms of use | Privacy Policy</span></div>
</div>
</body>
</html>
```